Design Letterhead + Business Card

Please refer to the attached document for the details to be included in the letterhead and business cards. Logo and contact details enclosed therein. Client is looking for a professional image.

Please include as many contact details as possible in your entries.

```html
<!DOCTYPE html>
<html lang="en">
<head>
<meta charset="utf-8">
<title>Cloudline Trading – Business Card</title>
<link rel="stylesheet" href="https://fonts.googleapis.com/css2?family=Arimo:wght@400;700&display=swap">
<style>
  :root {
    --page: #e6e7ea;
    --card: #ffffff;
    --sky: #1fb5ea;
    --sky-light: #bfe9fa;
    --sky-pale: #e6f7fd;
    --logo: #3aa9e0;
    --ink: #4a4a4a;
    --ink-dark: #222222;
    --navy: #1d3c7a;
  }
  * { margin: 0; padding: 0; box-sizing: border-box; }
  html, body { width: 1200px; height: 960px; overflow: hidden; background: var(--page); }
  body { position: relative; font-family: "Arimo", Arial, sans-serif; }

  .card {
    position: absolute;
    width: 620px; height: 350px;
    background: var(--card);
    border-radius: 12px;
    overflow: hidden;
    box-shadow: 0 2px 6px rgba(0,0,0,0.12);
  }
  .card--front { left: 90px; top: 110px; }
  .card--back { left: 490px; top: 530px; }
  .card-bands { position: absolute; inset: 0; width: 100%; height: 100%; }

  .brand { position: absolute; display: flex; align-items: center; gap: 14px; }
  .brand-dot { border-radius: 50%; background: var(--sky-light); flex: none; }
  .brand-name { color: var(--logo); font-weight: 400; letter-spacing: 0.5px; white-space: nowrap; }

  .card--front .brand { left: 120px; top: 110px; }
  .card--front .brand-dot { width: 130px; height: 130px; }
  .card--front .brand-name { font-size: 30px; }

  .front-web {
    position: absolute; right: 26px; bottom: 9px;
    font-size: 16px; font-weight: 700; color: var(--navy);
  }

  .card--back .brand { left: 350px; top: 74px; gap: 10px; }
  .card--back .brand-dot { width: 66px; height: 66px; }
  .card--back .brand-name { font-size: 16px; letter-spacing: 0.3px; }

  .holder { position: absolute; left: 52px; top: 82px; text-align: right; }
  .holder-name { font-size: 28px; font-weight: 700; color: var(--ink); line-height: 1; }
  .holder-role { font-size: 12px; color: var(--ink); letter-spacing: 0.5px; margin-top: 5px; }

  .contact-list { position: absolute; left: 32px; top: 196px; list-style: none; }
  .contact-list li {
    display: flex; align-items: center; gap: 12px;
    font-size: 14px; font-weight: 700; color: var(--ink-dark);
    height: 25px;
  }
  .contact-list svg { width: 16px; height: 16px; flex: none; }

  .address {
    position: absolute; left: 380px; top: 222px;
    font-size: 16px; font-weight: 700; color: var(--ink-dark); line-height: 1.3;
  }
</style>
</head>
<body>

<section class="card card--front" aria-label="Business card front">
  <svg class="card-bands" viewBox="0 0 620 350" aria-hidden="true">
    <defs>
      <linearGradient id="topFade" x1="0" y1="0" x2="0" y2="1">
        <stop offset="0" stop-color="#9fdcf6"/>
        <stop offset="1" stop-color="#e9f8fe"/>
      </linearGradient>
      <linearGradient id="bottomFade" x1="0" y1="0" x2="0" y2="1">
        <stop offset="0" stop-color="#e9f8fe"/>
        <stop offset="1" stop-color="#9fdcf6"/>
      </linearGradient>
    </defs>
    <path d="M0 0 H620 V12 H410 C392 12 388 32 368 32 H0 Z" fill="url(#topFade)"/>
    <path d="M408 14 H620 V24 H398 C402 20 403 14 408 14 Z" fill="#1fb5ea"/>
    <path d="M0 350 V336 H250 C272 336 276 314 300 314 H620 V350 Z" fill="url(#bottomFade)"/>
    <path d="M0 320 H272 C266 324 262 330 256 332 H0 Z" fill="#1fb5ea"/>
  </svg>
  <div class="brand">
    <span class="brand-dot"></span>
    <span class="brand-name">CLOUDLINE TRADING</span>
  </div>
  <p class="front-web">www.cloudlinetrading.co.za</p>
</section>

<section class="card card--back" aria-label="Business card back">
  <svg class="card-bands" viewBox="0 0 620 350" aria-hidden="true">
    <defs>
      <linearGradient id="topFadeB" x1="0" y1="0" x2="0" y2="1">
        <stop offset="0" stop-color="#9fdcf6"/>
        <stop offset="1" stop-color="#e9f8fe"/>
      </linearGradient>
      <linearGradient id="bottomFadeB" x1="0" y1="0" x2="0" y2="1">
        <stop offset="0" stop-color="#e9f8fe"/>
        <stop offset="1" stop-color="#9fdcf6"/>
      </linearGradient>
    </defs>
    <path d="M0 0 H620 V12 H410 C392 12 388 32 368 32 H0 Z" fill="url(#topFadeB)"/>
    <path d="M408 14 H620 V24 H398 C402 20 403 14 408 14 Z" fill="#1fb5ea"/>
    <path d="M0 350 V336 H250 C272 336 276 314 300 314 H620 V350 Z" fill="url(#bottomFadeB)"/>
    <path d="M0 320 H272 C266 324 262 330 256 332 H0 Z" fill="#1fb5ea"/>
  </svg>

  <div class="holder">
    <p class="holder-name">Lwazi Dlamini</p>
    <p class="holder-role">DIRECTOR / OWNER</p>
  </div>

  <div class="brand">
    <span class="brand-dot"></span>
    <span class="brand-name">CLOUDLINE TRADING</span>
  </div>

  <ul class="contact-list">
    <li>
      <svg viewBox="0 0 16 16" aria-hidden="true"><path d="M3.5 1.5 L6 4 L4.8 6 C5.6 7.8 8 10.2 10 11 L12 9.8 L14.5 12.3 L12.8 14.4 C7.5 14 2 8.5 1.6 3.2 Z" fill="#333"/></svg>
      071 555 0142
    </li>
    <li>
      <svg viewBox="0 0 16 16" aria-hidden="true"><rect x="3" y="1.5" width="10" height="13" rx="1" fill="none" stroke="#333" stroke-width="1.4"/><rect x="5" y="4" width="6" height="2" fill="#333"/><rect x="5" y="8" width="2" height="2" fill="#333"/><rect x="9" y="8" width="2" height="2" fill="#333"/><rect x="5" y="11" width="2" height="2" fill="#333"/><rect x="9" y="11" width="2" height="2" fill="#333"/></svg>
      0861 555 020
    </li>
    <li>
      <svg viewBox="0 0 16 16" aria-hidden="true"><rect x="1.5" y="3.5" width="13" height="9" fill="none" stroke="#333" stroke-width="1.3"/><path d="M1.5 3.5 L8 9 L14.5 3.5" fill="none" stroke="#333" stroke-width="1.3"/></svg>
      lwazi@cloudlinetrading.co.za
    </li>
    <li>
      <svg viewBox="0 0 16 16" aria-hidden="true"><circle cx="8" cy="8" r="6.5" fill="none" stroke="#333" stroke-width="1.2"/><ellipse cx="8" cy="8" rx="3" ry="6.5" fill="none" stroke="#333" stroke-width="1.1"/><path d="M1.5 8 H14.5 M2.5 5 H13.5 M2.5 11 H13.5" stroke="#333" stroke-width="1"/></svg>
      www.cloudlinetrading.co.za
    </li>
  </ul>

  <p class="address">Zone 9 No 41, Hillcrest,<br>Cape Town, Western Cape<br>7400</p>
</section>

</body>
</html>
```